Rocket business card

Modern business card design, use of color is good with clean space too.

Things to include on card:

Quote: I add fuel to your optometry practice

- Eyewear Sales
- Admin Duties
- Revenue Collection
- Leadership
- Tech Adoption
- COGS Reduction
- Product Sourcing
-Medical Growth

Dalton Vessey, CEO
Glint Harbor
Text Me! 847-302-1964
dalton@glintharbor.example

```html
<!DOCTYPE html>
<html lang="en">
<head>
<meta charset="utf-8">
<title>Glint Harbor – Business Card</title>
<link rel="stylesheet" href="https://fonts.googleapis.com/css2?family=Montserrat:wght@400;500;600&family=Raleway:wght@700&display=swap">
<style>
  :root {
    --backdrop: #8d8d8d;
    --card-dark: #1f1f1f;
    --deboss: #2e2e2e;
    --card-light: #ffffff;
    --ink: #111111;
    --text-grey: #4a4a4a;
    --accent-red: #e2402b;
    --accent-orange: #f07a2a;
    --accent-gold: #f5a02a;
  }
  * { box-sizing: border-box; margin: 0; padding: 0; }
  html, body {
    width: 1100px; height: 1200px; overflow: hidden;
    background: var(--backdrop);
    font-family: "Montserrat", Arial, sans-serif;
  }
  .card {
    position: absolute; left: 222px; width: 696px; height: 385px;
  }
  .card--back { top: 160px; background: var(--card-dark); }
  .card--front { top: 629px; background: var(--card-light); }

  /* back side */
  .back-mark {
    position: absolute; left: 50%; top: 96px; width: 120px; height: 120px;
    margin-left: -60px; border-radius: 50%;
    border: 4px solid var(--deboss);
  }
  .back-name {
    position: absolute; left: 0; right: 0; top: 228px; text-align: center;
    font-weight: 500; font-size: 42px; letter-spacing: 2px;
    color: var(--deboss); text-transform: uppercase;
  }

  /* front side */
  .brand {
    position: absolute; left: 40px; top: 120px; width: 280px; text-align: center;
  }
  .brand-dot {
    display: block; width: 62px; height: 62px; margin: 0 auto 16px;
    border-radius: 50%;
    background: linear-gradient(90deg, var(--accent-red), var(--accent-gold));
  }
  .brand-name {
    font-weight: 500; font-size: 31px; letter-spacing: 1px;
    color: var(--ink); text-transform: uppercase; white-space: nowrap;
  }
  .divider {
    position: absolute; left: 338px; top: 126px; width: 3px; height: 133px;
    background: var(--ink);
  }
  .contact { position: absolute; left: 365px; top: 122px; }
  .person-name {
    font-family: "Raleway", Arial, sans-serif; font-weight: 700;
    font-size: 27px; color: var(--accent-red); line-height: 1.1;
  }
  .person-role {
    font-weight: 600; font-size: 20px; color: var(--text-grey); line-height: 1.2;
  }
  .contact-list { list-style: none; margin-top: 24px; }
  .contact-item {
    display: flex; align-items: center; gap: 8px;
    font-size: 20.5px; color: var(--text-grey); line-height: 30px;
  }
  .contact-item svg { width: 20px; height: 16px; flex: none; }

  .services {
    position: absolute; left: 0; right: 0; top: 302px;
    list-style: none; display: flex; flex-wrap: wrap; justify-content: center;
    column-gap: 9px; row-gap: 4px; padding: 0 30px;
    font-size: 15.5px; color: var(--text-grey);
  }
  .services li { display: flex; align-items: center; gap: 4px; white-space: nowrap; }
  .services li::before {
    content: ""; width: 8px; height: 8px; border-radius: 50%;
    background: linear-gradient(90deg, var(--accent-red), var(--accent-orange));
  }
  .services .row-break { flex-basis: 100%; height: 0; }
  .services .row-break::before { display: none; }
</style>
</head>
<body>
  <section class="card card--back" aria-label="Card back">
    <span class="back-mark"></span>
    <p class="back-name">Glint Harbor</p>
  </section>

  <section class="card card--front" aria-label="Card front">
    <div class="brand">
      <span class="brand-dot"></span>
      <p class="brand-name">Glint Harbor</p>
    </div>
    <span class="divider"></span>
    <div class="contact">
      <h1 class="person-name">Dalton Vessey</h1>
      <p class="person-role">CEO</p>
      <ul class="contact-list">
        <li class="contact-item">
          <svg viewBox="0 0 20 16" aria-hidden="true">
            <path d="M1 5 Q10 -1 19 5 L16 7 L14 5 Q10 3 6 5 L4 7 Z" fill="var(--accent-red)"/>
            <path d="M5 8 L15 8 L18 15 L2 15 Z" fill="var(--accent-orange)"/>
            <circle cx="10" cy="11.5" r="2" fill="#fff"/>
          </svg>
          847-302-1964
        </li>
        <li class="contact-item">
          <svg viewBox="0 0 20 16" aria-hidden="true">
            <rect x="0.5" y="1" width="19" height="14" fill="var(--accent-orange)"/>
            <path d="M0.5 1 L10 9 L19.5 1 M0.5 15 L7.5 7 M19.5 15 L12.5 7" stroke="#fff" stroke-width="1.3" fill="none"/>
          </svg>
          dalton@glintharbor.example
        </li>
      </ul>
    </div>
    <ul class="services">
      <li>Eyewear Sales</li>
      <li>Admin Duties</li>
      <li>Revenue Collection</li>
      <li>Leadership</li>
      <li class="row-break" aria-hidden="true"></li>
      <li>Tech Adoption</li>
      <li>COGS Reduction</li>
      <li>Product Sourcing</li>
      <li>Medical Growth</li>
    </ul>
  </section>
</body>
</html>
```